Dental Office Needs- Flyer Design for Same Day Crowns

We need a flyer that will explain the benefits of the same day crown from the patient prospective. Not show pictures of the machine that makes the crowns. See attached material for content. The flyer should use the practices PMS colors of Green 562 and Blue 3025. The ad should say to the patient - I want to go this office and get my crown done there.
Updates

Project Deadline Extended Reason: The difference in the time zone between USA and Europe has caused issues. Minor changes still need to be worked out. Added Thursday, July 14, 2016

Target Market(s)

Dental Patients

Industry/Entity Type

Dental

Requirements
Must have
• Call to Action
• Business Address and Business Logo
• Classic Design
• images of a Happy 50 year old Couple
• Gives the benefits of the same day crown
Should not have
• No Images of tooth figures
• No before or after pictures

```html
<!DOCTYPE html>
<html lang="en">
<head>
<meta charset="utf-8">
<title>Same-Day Restorations Flyer</title>
<link href="https://fonts.googleapis.com/css2?family=Oswald:wght@400;500&family=Open+Sans:wght@400;600&family=Arimo:wght@400;700&display=swap" rel="stylesheet">
<style>
:root{
  --blue:#04587f;
  --navy:#0f4a78;
  --teal:#00846d;
  --lime:#a6cf3c;
  --step:#4f6a8c;
  --white:#ffffff;
  --divider:#ececec;
  --photo:#9a9a9a;
}
*{margin:0;padding:0;box-sizing:border-box}
html,body{width:1200px;height:927px;overflow:hidden;background:var(--white)}
.flyer{position:relative;width:1200px;height:927px;overflow:hidden;background:var(--white);font-family:"Open Sans",sans-serif}
.backdrop{position:absolute;left:0;top:0}
.panel-divider{position:absolute;top:0;width:1px;height:927px;background:var(--divider)}
.headline{position:absolute;left:66px;top:62px;font-family:"Oswald",sans-serif;line-height:1;color:var(--navy);font-weight:400}
.headline .big{font-size:62px;font-weight:500;letter-spacing:-1px;transform:scaleX(.86);transform-origin:left}
.headline .outline{display:block;color:transparent;-webkit-text-stroke:1.3px var(--navy);font-weight:400;transform:scaleX(.8);transform-origin:left}
.headline .mid{font-size:40px;margin:2px 0 0 80px}
.headline .visits{font-size:54px;margin:-2px 0 0 144px}
.intro{position:absolute;left:34px;top:320px;width:310px;text-align:center;color:var(--white);font-weight:600;font-size:19.5px;line-height:26.8px}
.copy{position:absolute;color:var(--navy)}
.copy h2{font-family:"Arimo",sans-serif;font-weight:700;font-size:24px;line-height:28px;margin-bottom:4px}
.copy p{font-size:16.5px;line-height:22px}
.copy .line{display:block;white-space:nowrap;text-align:justify;text-align-last:justify}
.copy .line.last{text-align-last:left}
.copy.same-day{left:420px;top:66px;width:360px}
.copy.same-day p{font-size:16px;line-height:21.9px}
.copy.scans{left:419px;top:371px;width:361px}
.copy.scans p{font-size:15.8px;line-height:21.9px}
.copy.results{left:825px;top:67px;width:280px}
.copy.results p{line-height:21.9px}
.portrait{position:absolute;left:820px;top:430px}
.steps-title{position:absolute;left:158px;top:753px;font-family:"Arimo",sans-serif;font-size:21px;color:var(--teal)}
.steps{position:absolute;left:0;top:796px}
.step-label{position:absolute;top:885px;width:80px;text-align:center;font-family:"Arimo",sans-serif;font-size:12.5px;color:var(--teal)}
.cta{position:absolute;left:869px;top:813px;font-family:"Arimo",sans-serif;font-size:18.5px;line-height:21px;color:var(--navy)}
.cta-band{position:absolute;left:800px;top:880px;width:400px;height:27px;background:linear-gradient(90deg,rgba(255,255,255,1) 0%,#a8c6d4 55%,#2f7a9b 100%)}
</style>
</head>
<body>
<main class="flyer">
  <svg class="backdrop" width="1200" height="927" viewBox="0 0 1200 927" aria-hidden="true">
    <circle cx="605" cy="18" r="600" fill="var(--lime)"/>
    <circle cx="575" cy="-20" r="592" fill="var(--white)"/>
    <circle cx="196" cy="420" r="164" fill="var(--teal)"/>
    <circle cx="189" cy="422" r="156" fill="var(--blue)"/>
  </svg>

  <div class="panel-divider" style="left:400px"></div>
  <div class="panel-divider" style="left:800px"></div>

  <h1 class="headline">
    <div class="big">2 HOURS</div>
    <span class="outline mid">INSTEAD OF</span>
    <span class="outline visits">2 VISITS.</span>
  </h1>

  <p class="intro">Introducing crowns,<br>veneers and bridges<br>that happen<br>in hours instead of<br>days-no more temporaries,<br>no more multiple visits,<br>no messy<br>dental impressions</p>

  <section class="copy same-day">
    <h2>Same-Day Density</h2>
    <p>
      <span class="line">Life is busy enough without having to make</span>
      <span class="line">multiple tips to the dentist overal several days,</span>
      <span class="line">Now with digital dentistry you get lab-quality</span>
      <span class="line">restorations in a single visit, First, we scan</span>
      <span class="line">your tooth rather than take a coventional</span>
      <span class="line">impression, Next a Custom restoration is</span>
      <span class="line">designed to fit your unique stmile, Then, your</span>
      <span class="line">crown, filling or veneers are created with</span>
      <span class="line">a state of the art milling unit right in our office</span>
      <span class="line">The final restoration is placed in your mouth</span>
      <span class="line last">the same day</span>
    </p>
  </section>

  <section class="copy scans">
    <h2>Digital Scans</h2>
    <p>
      <span class="line">The digital scanner uses state of the art laser</span>
      <span class="line">technology that is not only extremely precise</span>
      <span class="line">but also as safe as the checkout scanner at the</span>
      <span class="line">grocery store. Unlike conventional impressions</span>
      <span class="line">that can be messy, unplesant and cumbersome,</span>
      <span class="line last">adigital scan is clean, fast and comfortable.</span>
    </p>
  </section>

  <section class="copy results">
    <h2>Beautiful Results</h2>
    <p>The benefits of digital restorations<br>go beyond same day convenience.<br>Your restorations will also look and<br>feel completely natural. Digital<br>precision means a perfectly<br>comfortable fit. And, aesthetically,<br>your metal free restoration will<br>match the look of your teeth for a<br>beautiful, natural smile.</p>
  </section>

  <svg class="portrait" width="340" height="340" viewBox="0 0 340 340">
    <circle cx="170" cy="170" r="164" fill="var(--teal)"/>
    <circle cx="185" cy="174" r="148" fill="var(--photo)" role="img" aria-label="Photo of a smiling patient"/>
  </svg>

  <div class="steps-title">5 STEPS TO A BEAUTIFUL SMILE</div>
  <svg class="steps" width="620" height="80" viewBox="0 0 620 80" aria-hidden="true" fill="none" stroke="var(--step)" stroke-width="3">
    <g>
      <rect x="66" y="2" width="74" height="74" rx="8" stroke-width="4"/>
      <path d="M86 20h36v14H104v10H92V20z"/><path d="M98 44v22"/>
    </g>
    <g>
      <rect x="182" y="2" width="74" height="74" rx="8" stroke-width="4"/>
      <path d="M200 32l14-12h28"/><path d="M200 32h40"/><path d="M212 40l-6 10M218 40v12M224 40l6 10"/>
    </g>
    <g>
      <rect x="298" y="2" width="74" height="74" rx="8" stroke-width="4"/>
      <rect x="316" y="18" width="38" height="28" rx="2"/><path d="M310 56h50"/>
    </g>
    <g>
      <rect x="414" y="2" width="74" height="74" rx="8" stroke-width="4"/>
      <rect x="428" y="22" width="46" height="36" rx="3"/><rect x="440" y="26" width="18" height="10"/>
    </g>
    <g>
      <rect x="530" y="2" width="74" height="74" rx="8" stroke-width="4"/>
      <path d="M548 40l20 12h20M562 52l-4 14h20M582 14l-16 10"/>
    </g>
    <g fill="var(--step)">
      <path d="M146 39h20" fill="none"/><path d="M166 34l8 5-8 5z" stroke="none"/>
      <path d="M262 39h20" fill="none"/><path d="M282 34l8 5-8 5z" stroke="none"/>
      <path d="M378 39h20" fill="none"/><path d="M398 34l8 5-8 5z" stroke="none"/>
      <path d="M494 39h20" fill="none"/><path d="M514 34l8 5-8 5z" stroke="none"/>
    </g>
  </svg>
  <div class="step-label" style="left:60px">Prep</div>
  <div class="step-label" style="left:174px">Scan</div>
  <div class="step-label" style="left:292px">Design</div>
  <div class="step-label" style="left:406px">Mill</div>
  <div class="step-label" style="left:524px">Seat</div>

  <p class="cta">Ask your dentist<br>if a same day restoration<br>is right for you,</p>
  <div class="cta-band"></div>
</main>
</body>
</html>
```